Business Card for Wellness Clinic

We need a business card for our new logo. I want it to match the feel of the logo

Target Market(s)

Young professional families looking for holistic health care

Industry/Entity Type

Health And Wellness

Contact Information for Business Card

Our business Name: Brackenfield Health & wellness Centre, our phone #, email address...see attached old business card

Font styles to use
Sans Serif

Colors
33b8a4
cee9f5

Requirements
Must have
• my logo and business name
• Font is "Helvetica Neue LT Std 45 Light" and
• Only for "&" using font "Trajan pro bold"
• Use colors in the logo

```html
<!DOCTYPE html>
<html lang="en">
<head>
<meta charset="UTF-8">
<title>Brackenfield Health &amp; wellness Centre – Business Card</title>
<link rel="stylesheet" href="https://fonts.googleapis.com/css2?family=Lato:ital,wght@0,300;0,400;0,700;1,400&display=swap">
<style>
  :root {
    --teal: #33b8a4;
    --teal-soft: #cee9f5;
    --ink: #3d3e40;
    --grey-text: #a5a7aa;
    --rule: #6d6e70;
    --card: #ffffff;
    --backdrop: #b3b3b3;
  }
  * { box-sizing: border-box; margin: 0; padding: 0; }
  html, body {
    width: 1200px; height: 900px; overflow: hidden;
    background: var(--backdrop);
    font-family: "Lato", "Helvetica Neue", Arial, sans-serif;
  }
  .stage {
    width: 1200px; height: 900px;
    display: flex; flex-direction: column; align-items: center; justify-content: center;
    gap: 34px;
  }
  .card {
    position: relative;
    width: 700px; height: 400px;
    background: var(--card);
    box-shadow: 0 6px 18px rgba(0,0,0,0.22);
  }

  /* Brand name block (stands where the mark sits) */
  .brand {
    display: flex; align-items: center; gap: 14px;
    color: var(--teal); font-weight: 300;
  }
  .brand-square { width: 22px; height: 22px; background: var(--teal); flex: none; }
  .brand-name { font-size: 22px; line-height: 1.25; letter-spacing: 0.06em; text-transform: uppercase; }

  /* Front */
  .card-front .brand { position: absolute; left: 48px; top: 150px; width: 300px; }
  .name-tab {
    position: absolute; left: 350px; top: 62px; width: 280px; height: 60px;
    background: var(--ink); border-radius: 4px;
    padding: 9px 0 0 26px;
    box-shadow: 0 3px 6px rgba(0,0,0,0.3);
  }
  .name-tab .doctor { color: #fff; font-size: 17px; font-weight: 700; }
  .name-tab .doctor .creds { font-weight: 300; }
  .name-tab .role { color: var(--teal); font-size: 15px; font-weight: 300; margin-top: 2px; }
  .contact-list {
    position: absolute; left: 392px; top: 150px; list-style: none;
  }
  .contact-list li {
    display: flex; align-items: flex-start; gap: 16px;
    color: var(--teal); font-size: 15px; font-weight: 400; line-height: 1.25;
    margin-bottom: 8px;
  }
  .contact-list svg { width: 13px; height: 13px; flex: none; margin-top: 2px; fill: var(--ink); }

  /* Back */
  .card-back .brand { position: absolute; left: 50%; transform: translateX(-50%); top: 56px; width: max-content; }
  .card-back .brand-name { font-size: 20px; }
  .field-label { position: absolute; color: var(--teal); font-size: 19px; font-weight: 400; }
  .field-line { position: absolute; height: 1.5px; background: var(--rule); }
  .label-date { left: 56px; top: 148px; }
  .line-date { left: 50px; right: 50px; top: 176px; }
  .label-for { left: 56px; top: 196px; }
  .label-time { right: 80px; top: 196px; }
  .line-for { left: 50px; right: 50px; top: 236px; }
  .policy {
    position: absolute; left: 50px; right: 50px; top: 290px;
    color: var(--teal); font-style: italic; font-size: 14px; text-align: center; line-height: 1.5;
  }
</style>
</head>
<body>
<main class="stage">

  <section class="card card-front" aria-label="Business card front">
    <div class="brand">
      <span class="brand-square"></span>
      <span class="brand-name">Brackenfield Health &amp; wellness Centre</span>
    </div>

    <div class="name-tab">
      <p class="doctor">Dr. Maren Holt, <span class="creds">B.Sc., N.D.</span></p>
      <p class="role">Naturopathic Doctor</p>
    </div>

    <ul class="contact-list">
      <li>
        <svg viewBox="0 0 24 24" aria-hidden="true"><path d="M6.6 10.8a15.1 15.1 0 0 0 6.6 6.6l2.2-2.2a1 1 0 0 1 1-.25 11.4 11.4 0 0 0 3.6.57 1 1 0 0 1 1 1V20a1 1 0 0 1-1 1A17 17 0 0 1 3 4a1 1 0 0 1 1-1h3.5a1 1 0 0 1 1 1c0 1.25.2 2.45.57 3.6a1 1 0 0 1-.25 1z"/></svg>
        613-555-0142
      </li>
      <li>
        <svg viewBox="0 0 24 24" aria-hidden="true"><path d="M6 2h12v5H6z"/><path d="M3 8h18a1 1 0 0 1 1 1v8h-4v-3H6v3H2V9a1 1 0 0 1 1-1z"/><path d="M7 15h10v7H7z"/></svg>
        888-555-0187
      </li>
      <li>
        <svg viewBox="0 0 24 24" aria-hidden="true"><path d="M12 2a10 10 0 1 0 0 20 10 10 0 0 0 0-20zm0 2.2c1 1.2 1.8 3 2.1 5H9.9c.3-2 1.1-3.8 2.1-5zM4.4 13.2a7.8 7.8 0 0 1 0-2.4h3.3a17 17 0 0 0 0 2.4zm5.5 0a15 15 0 0 1 0-2.4h4.2a15 15 0 0 1 0 2.4zm2.1 6.6c-1-1.2-1.8-3-2.1-5h4.2c-.3 2-1.1 3.8-2.1 5zm4.3-6.6a17 17 0 0 0 0-2.4h3.3a7.8 7.8 0 0 1 0 2.4z"/></svg>
        www.brackenfieldwellness.ca
      </li>
      <li>
        <svg viewBox="0 0 24 24" aria-hidden="true"><path d="M2 6a2 2 0 0 1 2-2h16a2 2 0 0 1 2 2v.5l-10 6.3L2 6.5z"/><path d="M2 8.8l10 6.3 10-6.3V18a2 2 0 0 1-2 2H4a2 2 0 0 1-2-2z"/></svg>
        mholt@brackenfieldwellness.ca
      </li>
      <li>
        <svg viewBox="0 0 24 24" aria-hidden="true"><path d="M12 2a7 7 0 0 0-7 7c0 5.2 7 13 7 13s7-7.8 7-13a7 7 0 0 0-7-7zm0 9.5A2.5 2.5 0 1 1 12 6.5a2.5 2.5 0 0 1 0 5z"/></svg>
        <span>48 Linden Row, Suite 210<br>Northvale, ON K0A 2B4</span>
      </li>
    </ul>
  </section>

  <section class="card card-back" aria-label="Business card back, appointment reminder">
    <div class="brand">
      <span class="brand-square"></span>
      <span class="brand-name">Brackenfield Health &amp; wellness Centre</span>
    </div>

    <span class="field-label label-date">Date:</span>
    <span class="field-line line-date"></span>
    <span class="field-label label-for">For:</span>
    <span class="field-label label-time">Time:</span>
    <span class="field-line line-for"></span>

    <p class="policy">If you are unable to keep your appointment, please provide at least 2 business days notice or full visit fees will apply.</p>
  </section>

</main>
</body>
</html>
```